Baby Store - GIF Banner

About the Company:
Tolvi.com.sa is an online shop for baby related products in Saudi Arabia. The targeted audience is moms between 25-35 years of age. The word "Tolvi" means Shop/Store in the Arabic Language.
About the Banner:
The banners should be designed in animated GIF format and provide in four sizes, upon clicking on the banner it will take you to Tolvi website. The Banners will convey the following:
- All your baby daily needs
مستلزمات طفلك اليومية من تولفي
- Free same day delivery
توصيل مجاني بنفس اليوم في الرياض
- Subscribe now for special discounts.
سجلي الان لتحصلي على خصم خاص
Note: Arabic Text are attached in PSD format.
Design Requirements:
Company Logo is attached.
Sample of product photos will be provided.
Baby photo can be used.
Shop Now Button should be included in the design.
تسوق الان
Shop Now
Logo colors are the main colors to be used (Blue, Pink, Gray)
DropBox Link: will be provided upon request.
Design Style:
- Play full
- Feminine
- Creative
Delivery Requirements:
Initially we may start working on an English version, at the end you will must to provide an Arabic version of the Banners in addition to the English version. Arabic translations are provided above, Note that Arabic language is from right to left opposite to the English language.
Banners Sizes Required:
Banner 1: 728 x 90
Banner 2: 480 x 70
Banner 3: 300 x 250
Banner 4: 648x40
Banner Specs:
Size less than 100 kb
Background less than 80% alpha
Please pay EXTRA attention to the guidelines in the following link:
https://help.vexamora.com/clips/answer/531742
If you have any questions please let me know, wish you the best of luck.
Modern Moms of age 25-35.
Shop

```html
<!DOCTYPE html>
<html lang="en">
<head>
<meta charset="utf-8">
<title>Tolvi.com.sa – Leaderboard Banners</title>
<link rel="stylesheet" href="https://fonts.googleapis.com/css2?family=Montserrat:wght@400;500&display=swap">
<style>
  :root {
    --stage: #3a3839;
    --brand-blue: #4aa8e8;
    --brand-pink: #ec6aa6;
    --brand-pink-deep: #e35d9b;
    --logo-white: #ffffff;
    --text-white: #ffffff;
    --button-blue: #4aa6e6;
    --button-edge: #bfe0f7;
    --photo-skin: #e9c2a6;
    --photo-light: #f6e2d3;
    --pacifier-blue: #7fcbee;
    --pacifier-light: #d9f1fb;
  }
  * { box-sizing: border-box; margin: 0; padding: 0; }
  html, body { width: 1200px; height: 900px; overflow: hidden; }
  body {
    background: var(--stage);
    font-family: "Montserrat", Arial, sans-serif;
    position: relative;
  }
  .banner {
    position: absolute;
    left: 164px;
    width: 874px;
    height: 108px;
    background: var(--brand-pink);
    overflow: visible;
  }
  .banner--needs { top: 211px; }
  .banner--delivery { top: 396px; }
  .banner--subscribe { top: 576px; }

  .banner__clip {
    position: absolute; inset: 0; overflow: hidden;
  }
  .banner__logo-panel {
    position: absolute; left: 0; top: 0; width: 216px; height: 108px;
  }
  .banner__logo-panel svg { position: absolute; inset: 0; }
  .brand-name {
    position: absolute;
    left: 16px; top: 38px;
    font-weight: 500;
    font-size: 24px;
    color: var(--brand-blue);
    letter-spacing: -0.2px;
  }
  .headline {
    position: absolute;
    left: 260px; top: 8px;
    color: var(--text-white);
    font-weight: 500;
    font-size: 35px;
    line-height: 44px;
  }
  .headline__caps { text-transform: uppercase; display: block; }

  .photo-baby {
    position: absolute; right: 0; top: 0;
    width: 160px; height: 108px;
    background: radial-gradient(ellipse at 55% 45%, var(--photo-light) 0%, var(--photo-skin) 55%, var(--brand-pink) 100%);
  }
  .photo-pacifier {
    position: absolute; left: 670px; top: -6px;
    width: 176px; height: 114px;
    border-radius: 50% 40% 50% 45%;
    background: radial-gradient(ellipse at 45% 50%, var(--pacifier-light) 0%, var(--pacifier-blue) 60%, rgba(127,203,238,0) 100%);
  }

  .cta-button {
    position: absolute;
    left: 235px; top: 30px;
    width: 228px; height: 49px;
    background: var(--button-blue);
    border: 2px solid var(--button-edge);
    border-radius: 4px;
    color: var(--text-white);
    font-weight: 500;
    font-size: 19px;
    display: flex; align-items: center; justify-content: center;
    text-transform: uppercase;
    letter-spacing: 0.2px;
  }
  .cta-tail {
    position: absolute;
    left: 480px; top: 31px;
    color: var(--text-white);
    font-weight: 500;
    font-size: 35px;
    line-height: 44px;
    white-space: nowrap;
  }
</style>
</head>
<body>

  <section class="banner banner--needs" aria-label="All your baby daily needs">
    <div class="banner__clip">
      <div class="banner__logo-panel">
        <svg width="216" height="108" viewBox="0 0 216 108" aria-hidden="true">
          <path d="M0 0 H200 Q188 54 196 108 H0 Z" fill="var(--logo-white)"/>
          <path d="M200 0 H214 Q202 54 210 108 H196 Q188 54 200 0 Z" fill="var(--brand-blue)"/>
        </svg>
        <span class="brand-name">Tolvi.com.sa</span>
      </div>
      <p class="headline">All your baby<span class="headline__caps">Daily needs</span></p>
      <div class="photo-baby" role="img" aria-label="Photo of a smiling baby holding a teether"></div>
    </div>
  </section>

  <section class="banner banner--delivery" aria-label="Free same day delivery">
    <div class="banner__clip">
      <div class="banner__logo-panel">
        <svg width="216" height="108" viewBox="0 0 216 108" aria-hidden="true">
          <path d="M0 0 H200 Q188 54 196 108 H0 Z" fill="var(--logo-white)"/>
          <path d="M200 0 H214 Q202 54 210 108 H196 Q188 54 200 0 Z" fill="var(--brand-blue)"/>
        </svg>
        <span class="brand-name">Tolvi.com.sa</span>
      </div>
      <p class="headline">Free same day<span class="headline__caps">Delivery</span></p>
    </div>
    <div class="photo-pacifier" role="img" aria-label="Product photo of a blue pacifier"></div>
  </section>

  <section class="banner banner--subscribe" aria-label="Subscribe now for special discounts">
    <div class="banner__clip">
      <div class="banner__logo-panel">
        <svg width="216" height="108" viewBox="0 0 216 108" aria-hidden="true">
          <path d="M0 0 H200 Q188 54 196 108 H0 Z" fill="var(--logo-white)"/>
          <path d="M200 0 H214 Q202 54 210 108 H196 Q188 54 200 0 Z" fill="var(--brand-blue)"/>
        </svg>
        <span class="brand-name">Tolvi.com.sa</span>
      </div>
      <span class="cta-button">Subscribe now</span>
      <p class="cta-tail">for special discounts</p>
    </div>
  </section>

</body>
</html>
```